Builder and developer needs website

I am re-establishing my building company after 15 years of managing other peoples building companies.
My main focus is building medium density housing with other investors as part of a syndicate. My current website is hopeless and cant be found by Google or Yahoo. It is www.dunmorebuildgroup.net.au

I have a couple of websites that I have seen that are a good inspiration for me.

I have looked at the Telvor Developments site http://www.telvor.com.au/ and like what I see. They offer the same development service that I want to offer. I also want to have a membership page/area for trades.
• The site is not wordy. It is glam and emotive
• The links to each page are easy to see and follow.
• The home page has the large images at the bottom that direct you into the emotional areas i.e. what we are building, discover the possibilities and expression of interest.
• The “Services” page is great. No long stories. Just click on the image you want to read about and off you go.
• There are a few links that don’t direct you to the correct pages i.e. expression of interest.
• There are a few places where they capture your contact details.

Also the property strategies page http://www.yieldpathways.net/bright-yield-pathways of the BYP site is very relevant to my goals. This site has a similar message but is far wordier explaining it. The research part of me likes this site as it explains more. It also uses emotive description.
The one annoying thing is the “Holdings Accelerant” sends you to a page with no tabs above to move to another page and “Estate Inner Circle” sends you to another site. I suppose his aim is to get paying people to his education courses and into his syndicates.

There is also Darryl Pendleby’s site http://darrylpendlebyestates.com.au/services/ It is hard to read due to the colours. Again it is wordy, but it is educational.

My preference is using the template of the Telvor “services” page and each wordy piece is a link.
Updates

Hello Contestants

My old website was for my old profile as a builder only. Now I want to be seen as a builder and developer as per the Telvor web site. I will be developing property just like that site and the BYP site and the Darryl Pendleby site. Thanks

Regards
Nigel Forster

Target Market(s)

Target market is people that want an investment property portfolio.
Have a SMSF or Self Managed Super Fund and want property to diversify their portfolio.
People wanting to aim for early retirement and spending time with family or working for worthwhile causes.
Have a reasonable risk profile.
Have imagination and can see how a syndicate works and the benefits for everyone.
Have imagination and can picture the finished product.
Prefer not to pay retail for property.
Prepared to wait for units to be constructed.
People that want others/joint partners around them to be come wealthy as well.

Industry/Entity Type

Education

Requirements
Nice to have
• Clear and easy navigation of the web site.
The site will be used by people in their late 30's upwards.
Sophistication
Easy maintenance of the site by me. I have limited skills in this department.
Easy SEO finding as my current site is hopeless
A members page for investors
A way of getting emails for a data base.
Should not have
• Flashing lights.
Spelling errors.
Loud noises
Background that makes the text difficult to read.

```html
<!DOCTYPE html>
<html lang="en">
<head>
<meta charset="utf-8">
<title>Dunmore Constructions</title>
<link href="https://fonts.googleapis.com/css2?family=Arimo:wght@400;700&family=Open+Sans:wght@400;600&family=Playfair+Display+SC:wght@400;700&family=Roboto+Condensed:wght@400;700&display=swap" rel="stylesheet">
<style>
  :root{
    --header-bg:#2c2f34;
    --panel-bg:#33363b;
    --field-bg:#1f2124;
    --brand-blue:#1b6fc0;
    --label-blue:#1a63b0;
    --arrow-green:#22a65a;
    --tick-green:#2aa84a;
    --ink:#2a2a2a;
    --heading-ink:#222;
    --rule:#d8d8d8;
    --hex-red:#e31e24;
    --footer-bg:#36383b;
    --badge-bg:#4a4d52;
    --bottom-bg:#1c1d1f;
    --white:#ffffff;
  }
  *{box-sizing:border-box;margin:0;padding:0}
  html,body{width:860px;height:1200px;overflow:hidden;background:var(--white)}
  .canvas{position:relative;width:860px;height:1200px;overflow:hidden;font-family:"Roboto Condensed",Arial,sans-serif;color:var(--ink)}

  /* header */
  .site-header{position:absolute;left:0;top:0;width:860px;height:78px;background:linear-gradient(180deg,#26292d,#34373c)}
  .brand{position:absolute;left:52px;top:16px;display:flex;align-items:center;gap:8px}
  .brand-mark{width:20px;height:20px;background:var(--brand-blue)}
  .brand-name{font-family:"Arimo",Arial,sans-serif;font-weight:700;font-size:28px;color:var(--brand-blue);letter-spacing:.5px}
  .nav-rule{position:absolute;left:437px;top:23px;width:379px;height:3px;background:var(--white)}
  .nav-rule::before{content:"";position:absolute;left:0;top:0;width:33px;height:3px;background:var(--brand-blue)}
  .main-nav{position:absolute;right:44px;top:37px;display:flex;gap:17px;font-family:"Arimo",Arial,sans-serif;font-size:13.5px;color:var(--white)}

  /* hero */
  .hero{position:absolute;left:0;top:78px;width:860px;height:397px}
  .signup-panel{position:absolute;left:0;top:0;width:258px;height:397px;background:linear-gradient(180deg,#3a3d42,#2a2c30)}
  .panel-rule{position:absolute;left:16px;top:23px;width:226px;height:1px;background:linear-gradient(90deg,transparent,#bbb,transparent)}
  .panel-rule::after{content:"";position:absolute;left:107px;top:-2px;width:12px;height:5px;border-radius:3px;background:#ccc}
  .field-label{position:absolute;left:46px;font-family:"Open Sans",sans-serif;font-size:13px;color:var(--white)}
  .field{position:absolute;left:40px;width:183px;height:29px;border-radius:12px;background:var(--field-bg);box-shadow:inset 0 1px 3px #000}
  .signup-btn{position:absolute;left:82px;top:248px;width:77px;height:77px;border-radius:50%;background:#2a2c30;border-bottom:3px solid var(--brand-blue);box-shadow:0 2px 4px rgba(0,0,0,.6);display:flex;align-items:center;justify-content:center;font-family:"Open Sans",sans-serif;font-size:18px;color:var(--white)}
  .hero-photo{position:absolute;left:258px;top:0;width:602px;height:397px;background:linear-gradient(160deg,#3b4654 0%,#c89a60 38%,#e8c690 55%,#3f8fc8 72%,#1e6fae 100%)}
  .slider-dots{position:absolute;left:453px;top:381px;display:flex;gap:3px}
  .slider-dots span{width:8px;height:8px;border-radius:50%;background:#333}
  .slider-dots span:first-child{background:var(--white);border:1px solid #333}

  /* content */
  .section-title{position:absolute;font-family:"Playfair Display SC",Georgia,serif;font-weight:700;font-size:17px;color:var(--heading-ink);letter-spacing:.4px}
  .service-list{position:absolute;list-style:none;font-size:12.5px;line-height:18.5px}
  .service-list li{position:relative;padding-left:30px;margin-bottom:6.5px}
  .service-list li::before{content:"";position:absolute;left:2px;top:2px;width:18px;height:14px;background:var(--arrow-green);clip-path:polygon(0 0,100% 50%,0 100%,28% 50%)}
  .label{color:var(--label-blue);font-weight:700;font-variant:small-caps;letter-spacing:.3px;margin-right:6px}
  .column-divider{position:absolute;left:423px;top:500px;width:1px;height:180px;background:var(--rule)}
  .assurance-list{position:absolute;left:16px;top:862px;list-style:none;font-size:12.5px;line-height:20px}
  .assurance-list li{display:flex;align-items:center;gap:14px}
  .assurance-list svg{width:14px;height:14px}

  /* social band */
  .social-band{position:absolute;left:0;top:1046px;width:860px;height:28px;background:var(--brand-blue)}
  .social-links{position:absolute;left:306px;top:1024px;display:flex;gap:9px}
  .social-links span{width:42px;height:46px;background:var(--hex-red);clip-path:polygon(50% 0,100% 25%,100% 75%,50% 100%,0 75%,0 25%)}

  /* footer */
  .site-footer{position:absolute;left:0;top:1074px;width:860px;height:106px;background:var(--footer-bg);color:var(--white)}
  .member-badge{position:absolute;left:122px;top:26px;width:210px;height:58px;border-radius:6px;background:var(--badge-bg)}
  .newsletter{position:absolute;left:368px;top:42px}
  .newsletter h3{font-family:"Arimo",Arial,sans-serif;font-weight:400;font-size:17px;margin-bottom:10px}
  .newsletter .field{position:static;display:block;width:162px;height:20px;border-radius:0;background:#efefef;box-shadow:none}
  .contact-details{position:absolute;left:545px;top:18px;list-style:none;font-family:"Arimo",Arial,sans-serif;font-size:8.5px;line-height:10px}
  .contact-details li{position:relative;padding-left:17px;margin-bottom:10px}
  .contact-details svg{position:absolute;left:0;top:0;width:10px;height:10px}
  .bottom-bar{position:absolute;left:0;top:1180px;width:860px;height:20px;background:var(--bottom-bg);color:var(--white);font-family:"Arimo",Arial,sans-serif;font-size:8px;text-align:center;line-height:20px}
</style>
</head>
<body>
<div class="canvas">

  <header class="site-header">
    <div class="brand"><span class="brand-mark"></span><span class="brand-name">Dunmore</span></div>
    <div class="nav-rule"></div>
    <nav class="main-nav"><span>Home</span><span>About</span><span>Services</span><span>Portfolio</span><span>Gallery</span><span>Blog</span><span>Contact</span></nav>
  </header>

  <section class="hero">
    <form class="signup-panel">
      <div class="panel-rule"></div>
      <label class="field-label" style="top:92px">Name</label>
      <div class="field" style="top:107px"></div>
      <label class="field-label" style="top:165px">Email</label>
      <div class="field" style="top:183px"></div>
      <div class="signup-btn">Sign Up</div>
    </form>
    <div class="hero-photo" role="img" aria-label="Modern waterfront home with lit living area and infinity pool at dusk"></div>
    <div class="slider-dots"><span></span><span></span><span></span><span></span><span></span><span></span></div>
  </section>

  <h2 class="section-title" style="left:13px;top:496px">Construction:</h2>
  <ul class="service-list" style="left:13px;top:532px;width:405px">
    <li><span class="label">Renovations &amp; Extensions:</span>Structural renovations and extensions.</li>
    <li><span class="label">New Homes:</span>We have the flexibility to build to any design.</li>
    <li><span class="label">Dual Occupancies:</span>Construction only / Turn Key / or Full Development:</li>
    <li><span class="label">Villas:</span>Design, town planning approvals, and construction.</li>
    <li><span class="label">Townhouse developments:</span></li>
    <li><span class="label">Boutique Unit developments:</span></li>
  </ul>

  <div class="column-divider"></div>

  <h2 class="section-title" style="left:445px;top:496px">Residential Development Management:</h2>
  <ul class="service-list" style="left:445px;top:532px;width:410px">
    <li><span class="label">Approvals:</span>Site capacity/feasibility, selection of design consultants, design supervision, town planning approvals.</li>
    <li><span class="label">Construction:</span>Construction documentation, select and open tender process and assessment, construction supervision, reporting and documentation.</li>
    <li><span class="label">Project Partnership:</span>Design, town planning approvals, construction and marketing. We are always interested in discussing ethical and mutually beneficial project partnerships or property options</li>
  </ul>

  <h2 class="section-title" style="left:13px;top:695px">Commercial Construction Supervision:</h2>
  <ul class="service-list" style="left:13px;top:731px;width:835px">
    <li><span class="label" style="margin-right:30px">Project Management</span>Experience covers the successful project management of the construction of school buildings, police stations, ambulance stations and fire stations</li>
    <li><span class="label" style="margin-right:22px">Site Management</span>Experience covers prestige cinema complex, landmark medical research building, Coastal Mail sorting centre, fit out of a 24 floor apartment building, a number of multi-storey apartment buildings, school buildings, landscaping and civil supervision.</li>
  </ul>

  <h2 class="section-title" style="left:14px;top:827px">Construction Partner Assurance:</h2>
  <ul class="assurance-list">
    <li><svg viewBox="0 0 14 14"><path d="M1 8l4 4L13 1" fill="none" stroke="var(--tick-green)" stroke-width="2.5"/></svg>An initial design and building consultation to ensure best building practice and to mitigate any foreseeable site issues;</li>
    <li><svg viewBox="0 0 14 14"><path d="M1 8l4 4L13 1" fill="none" stroke="var(--tick-green)" stroke-width="2.5"/></svg>A fixed price contract to ensure your budget is maintained;</li>
    <li><svg viewBox="0 0 14 14"><path d="M1 8l4 4L13 1" fill="none" stroke="var(--tick-green)" stroke-width="2.5"/></svg>Reliable and punctual service and we will do everything in our power to ensure your project is completed on time;</li>
    <li><svg viewBox="0 0 14 14"><path d="M1 8l4 4L13 1" fill="none" stroke="var(--tick-green)" stroke-width="2.5"/></svg>A clean and safe building site;</li>
    <li><svg viewBox="0 0 14 14"><path d="M1 8l4 4L13 1" fill="none" stroke="var(--tick-green)" stroke-width="2.5"/></svg>Clear communication with regular progress updates; and</li>
    <li><svg viewBox="0 0 14 14"><path d="M1 8l4 4L13 1" fill="none" stroke="var(--tick-green)" stroke-width="2.5"/></svg>QLD and NSW Builders Licence, construction insurance and BMA membership.</li>
  </ul>

  <div class="social-band"></div>
  <div class="social-links"><span></span><span></span><span></span><span></span><span></span></div>

  <footer class="site-footer">
    <div class="member-badge" role="img" aria-label="Builders association membership badge"></div>
    <div class="newsletter"><h3>Join our newsletter</h3><span class="field"></span></div>
    <ul class="contact-details">
      <li><svg viewBox="0 0 10 10"><path d="M5 1L1 5h1.5v4h5V5H9z" fill="#777"/></svg>Nigel Forster<br>Servicing:<br>South East QLD &amp; Northern NSW</li>
      <li><svg viewBox="0 0 10 10"><rect x="1" y="2.5" width="8" height="5.5" fill="#777"/></svg>info@dunmore.net.au</li>
      <li><svg viewBox="0 0 10 10"><path d="M1 4q4-4 8 0l-1.5 1.5-1.5-1v-1h-2v1l-1.5 1z M2 6h6v3H2z" fill="#777"/></svg>0412 386 905</li>
    </ul>
  </footer>
  <div class="bottom-bar">© 2014 Dunmore Constructions Ltd</div>

</div>
</body>
</html>
```